New Business Card Design Project

I would like a business card to match my truck wrap and logo. I would like the font to match my existing business card please.

Industry/Entity Type

Painter

Contact Information for Business Card

Rodrigo Venter 801-437-2910 Ventercoatings.utah@brushmail.net
SERVICES - Custom Paint & Stain, Interior & Exterior, Epoxy Coatings / Garage Floors, Cabinet Refinishing, Log Staining and Refinishing.

Requirements
Nice to have
• I would like to have the white and grey line like the bottom of my vehicle wrap, Light Grey to match my truck also.

```html
<!DOCTYPE html>
<html lang="en">
<head>
<meta charset="utf-8">
<title>Venter Coatings – Business Card</title>
<link rel="stylesheet" href="https://fonts.googleapis.com/css2?family=Montserrat:wght@400;500;600&family=Oswald:wght@500&display=swap">
<style>
  :root {
    --bg: #1c1c1c;
    --card: #222222;
    --card-edge: #2a2a2a;
    --accent: #12a8e8;
    --text: #f2f2f2;
    --muted: #c9c9c9;
  }
  * { margin: 0; padding: 0; box-sizing: border-box; }
  html, body { width: 1200px; height: 900px; overflow: hidden; }
  body {
    background: var(--bg);
    font-family: "Montserrat", sans-serif;
    color: var(--text);
    display: flex;
    flex-direction: column;
    align-items: center;
    justify-content: center;
    gap: 40px;
  }
  .card {
    position: relative;
    width: 680px;
    height: 390px;
    padding: 0 40px;
    background: linear-gradient(135deg, var(--card) 0%, var(--card-edge) 100%);
    border-bottom: 6px solid var(--accent);
    box-shadow: 0 10px 30px rgba(0,0,0,.5);
  }
  /* front */
  .card--front { display: flex; flex-direction: column; align-items: center; justify-content: center; }
  .brand { display: flex; align-items: center; gap: 18px; margin-bottom: 42px; }
  .brand__mark { width: 54px; height: 54px; background: var(--accent); }
  .brand__name { font-weight: 600; font-size: 40px; letter-spacing: 4px; color: var(--muted); text-transform: uppercase; white-space: nowrap; }
  .services__title { color: var(--accent); font-weight: 500; font-size: 19px; letter-spacing: 2px; text-align: center; margin-bottom: 6px; }
  .services__list { text-align: center; font-size: 15.5px; line-height: 1.6; }
  .sep { color: var(--accent); margin: 0 4px; }
  /* back */
  .card--back { display: flex; align-items: center; justify-content: center; gap: 22px; }
  .person { text-align: right; white-space: nowrap; }
  .person__name { font-family: "Oswald", sans-serif; font-weight: 500; font-size: 36px; color: var(--accent); text-transform: uppercase; letter-spacing: 1px; line-height: 1.1; }
  .person__role { font-size: 17px; }
  .divider { width: 2px; height: 84px; background: var(--accent); flex: none; }
  .contacts { list-style: none; font-size: 15.5px; line-height: 1.7; white-space: nowrap; }
  .contacts li { display: flex; align-items: center; gap: 9px; }
  .contacts svg { width: 13px; height: 13px; flex: none; }
</style>
</head>
<body>
  <section class="card card--front">
    <div class="brand">
      <span class="brand__mark"></span>
      <span class="brand__name">Venter Coatings</span>
    </div>
    <h2 class="services__title">SERVICES</h2>
    <p class="services__list">
      Custom Paint &amp; Stain<span class="sep">|</span>Interior &amp; Exterior<span class="sep">|</span>Epoxy Coatings / Garage Floors<br>
      Cabinet Refinishing<span class="sep">|</span>Log Staining and Refinishing.
    </p>
  </section>

  <section class="card card--back">
    <div class="person">
      <h1 class="person__name">Rodrigo Venter</h1>
      <p class="person__role">Director</p>
    </div>
    <span class="divider"></span>
    <ul class="contacts">
      <li>
        <svg viewBox="0 0 16 16" aria-hidden="true"><path fill="#12a8e8" d="M3.6 1.2l2.3 2.6-1.3 1.8c.9 2 2.3 3.4 4.3 4.3l1.8-1.3 2.6 2.3-1.6 2.4C6.6 13.2 2.8 9.4 1.2 4.3z"/></svg>
        801-437-2910
      </li>
      <li>
        <svg viewBox="0 0 16 16" aria-hidden="true"><rect x="1.5" y="3.5" width="13" height="9" fill="none" stroke="#12a8e8" stroke-width="1.5"/><path d="M1.5 3.5l6.5 5 6.5-5" fill="none" stroke="#12a8e8" stroke-width="1.5"/></svg>
        Ventercoatings.utah@brushmail.net
      </li>
      <li>
        <svg viewBox="0 0 16 16" aria-hidden="true"><g fill="none" stroke="#12a8e8" stroke-width="1.3"><circle cx="8" cy="8" r="6.3"/><ellipse cx="8" cy="8" rx="2.8" ry="6.3"/><path d="M1.7 8h12.6M2.8 4.6h10.4M2.8 11.4h10.4"/></g></svg>
        www.ventercoatings.utah.com
      </li>
    </ul>
  </section>
</body>
</html>
```